Rivolex.com Trucking Company Website

Need a website designed (no content) for a trucking company, specializing in trucking of ocean containers (intermodal Trucking). Heavy emphasis on technology, using latest technology, providing unabated visibility and realtime information.
clean minimalist industrial website
example:
https://www.bramtiq.com/

Target Market(s)

Professional Business Consumer corporate and small business

Industry/Entity Type

Trucking Company

Number of Pages Required

5+ page

Requirements
Must have
• Industrial Design, simple informative, for a busy professional to view and get the necessary information with out the distractions.
• Blog Page
• Client Log-In on the front page
• Technology page - showing our intensive investments in technology
Nice to have
• If ANY images included, MUST be USA related. Example if include an image of a truck, ensure its a USA model. Do the research.
• included our business card for sample of Logo
• Doesnt not have to be the same color schemes.
Should not have
• moving images

```html
<!DOCTYPE html>
<html lang="en">
<head>
<meta charset="utf-8">
<title>Rivolex Consulting – Home</title>
<link href="https://fonts.googleapis.com/css2?family=Open+Sans:wght@300;400;600;700&display=swap" rel="stylesheet">
<style>
  :root {
    --page-bg: #ffffff;
    --brand-blue: #1e6fc0;
    --nav-active: #2b79c3;
    --sidebar-veil: rgba(246, 246, 246, 0.9);
    --ink: #2b2b2b;
    --light-text: #ffffff;
    --social-rss: #f5bd4c;
    --social-bird: #3fa6dc;
    --social-ball: #e06c9b;
    --social-video: #64cbd9;
    --social-book: #4a69b6;
  }
  * { margin: 0; padding: 0; box-sizing: border-box; }
  html, body {
    width: 1200px; height: 1120px; overflow: hidden;
    background: var(--page-bg);
    font-family: "Open Sans", Arial, sans-serif;
  }
  .hero {
    position: absolute; left: 0; top: 220px;
    width: 1200px; height: 678px; overflow: hidden;
  }
  .hero-photo {
    position: absolute; inset: 0;
    background:
      linear-gradient(180deg, rgba(0,0,0,0) 0%, rgba(0,0,0,0) 78%, #7d7d79 85%, #6a6b68 100%),
      linear-gradient(100deg, #6e4a2e 0%, #5a4526 30%, #4a4424 55%, #5b4a2a 75%, #6a5634 100%);
  }
  .sidebar {
    position: absolute; left: 38px; top: 0;
    width: 292px; height: 678px;
    background: var(--sidebar-veil);
  }
  .brand {
    position: absolute; top: 58px; left: 0; width: 100%;
    text-align: center;
    font-size: 38px; font-weight: 700; letter-spacing: 0.04em;
    color: var(--brand-blue);
  }
  .main-nav { list-style: none; }
  .main-nav li {
    position: absolute; left: 0; width: 100%;
    text-align: center;
    font-size: 16px; letter-spacing: 0.42em;
    color: var(--ink);
    height: 39px; line-height: 39px;
    padding-left: 0.42em;
  }
  .main-nav li.is-active { background: var(--nav-active); color: var(--light-text); }
  .social {
    position: absolute; top: 619px; left: 47px;
    display: flex; gap: 12px;
  }
  .social span { width: 30px; height: 30px; border-radius: 3px; display: block; }
  .social .rss { background: var(--social-rss); }
  .social .bird { background: var(--social-bird); }
  .social .ball { background: var(--social-ball); }
  .social .video { background: var(--social-video); }
  .social .book { background: var(--social-book); }
  .welcome {
    position: absolute; left: 692px; top: 148px; width: 505px;
    color: var(--light-text);
  }
  .welcome-kicker { font-size: 21px; font-weight: 400; line-height: 1.2; }
  .welcome-title {
    font-size: 47px; font-weight: 300; color: var(--brand-blue);
    line-height: 1.05; white-space: nowrap;
  }
  .welcome-copy { font-size: 13.6px; line-height: 32.5px; margin-top: 12px; }
  .login-btn {
    position: absolute; left: 686px; top: 374px;
    width: 178px; height: 39px; line-height: 39px;
    background: var(--brand-blue); color: var(--light-text);
    text-align: center; font-size: 13.5px; font-weight: 400;
  }
  .site-footer {
    position: absolute; right: 5px; top: 654px;
    font-size: 11.5px; font-weight: 700; color: var(--light-text);
    word-spacing: 1px;
  }
  .site-footer .sep { margin: 0 14px; }
</style>
</head>
<body>
  <section class="hero">
    <div class="hero-photo" role="img" aria-label="Photo of a white American semi truck driving along an autumn forest highway"></div>

    <aside class="sidebar">
      <div class="brand">RIVOLEX</div>
      <ul class="main-nav">
        <li class="is-active" style="top:155px">HOME</li>
        <li style="top:226px">ABOUT US</li>
        <li style="top:297px">SERVICES</li>
        <li style="top:367px">TECHNOLOGY</li>
        <li style="top:438px">BLOG</li>
      </ul>
      <div class="social" aria-label="Social links">
        <span class="rss"></span>
        <span class="bird"></span>
        <span class="ball"></span>
        <span class="video"></span>
        <span class="book"></span>
      </div>
    </aside>

    <div class="welcome">
      <p class="welcome-kicker">WELCOME TO</p>
      <h1 class="welcome-title">RIVOLEX CONSULTING</h1>
      <p class="welcome-copy">Lorem Ipsum is simply dummy text of the printing and typesetting industry. Lorem Ipsum has been the industry's standard dummy text ever since the 1500s, when an unknown printer took a galley of type and scrambled it to make a type specimen book. It has survived not only five centuries,</p>
    </div>

    <div class="login-btn">LOGIN</div>

    <footer class="site-footer">Copyright © 2017<span class="sep">|</span>Rivolex Consulting Inc<span class="sep">|</span>All rights reserved.</footer>
  </section>
</body>
</html>
```